Business Card Design - Local Loss Adjusting Office

Please read the description! We will provide an example of one concept with all required information that needs organization. Other concepts has to be your own design. We would require icons - if it fits the design - instead of letters when it comes to Telephone, Mobile, Fax, etc. The design has to be elegant, modern, and simple. We need the Photoshop/Illustrator files in latest version with layers. We would require a PDF of the cards as well a JPG version. The font used should be Calibri. The colors are included in the first concept sample attached. The name - the person name only that is - should be put in duplicate because we will use another language in one of the lines The card size is 5.5cm x 8.5cm. If you need anything else, please let us know. Thank you.
Reason: Most designers haven't read the project description properly!
Hi All,
We need to choose one design tomorrow, and would like to bring to your attention the following:
1- We are Velorin Adjusting not Dorian Whitfield! We are exclusive local representative of Dorian Whitfield. This should only be on the back side of the card.
2- We will use bilingual names for employees. Therefore put a duplicate English name, we will change one to another language with our in house designer afterwards.
3- All icons should be on the left side of text never on the right.
4- Don't change the logo colors please.
5- Dont overcrowd the card with colors. Simple, elegant, and modern please.
Sorry for not being able to respond to all inquires as we have 100+ submissions.
Goodluck to all.
Best regards,
Velorin

```html
<!DOCTYPE html>
<html lang="en">
<head>
<meta charset="utf-8">
<title>Velorin Adjusting – Business Card</title>
<link rel="stylesheet" href="https://fonts.googleapis.com/css2?family=Carlito:ital,wght@0,400;0,700;1,400&display=swap">
<style>
  :root {
    --page: #e7e7e7;
    --card: #ffffff;
    --green: #a9cb62;
    --ink: #2f2f2f;
    --white: #ffffff;
    --divider: rgba(255,255,255,0.45);
  }
  * { margin: 0; padding: 0; box-sizing: border-box; }
  html, body { width: 1200px; height: 1145px; overflow: hidden; }
  body {
    background: var(--page);
    font-family: "Carlito", "Calibri", sans-serif;
    position: relative;
  }
  .card {
    position: absolute;
    left: 60px;
    width: 704px;
    height: 456px;
    background: var(--card);
    overflow: hidden;
  }
  .card--front { top: 96px; }
  .card--back { top: 624px; }

  .wordmark {
    position: absolute;
    display: flex;
    flex-direction: column;
    align-items: flex-end;
    color: var(--ink);
    font-weight: 700;
    line-height: 0.9;
  }
  .card--front .wordmark { right: 51px; top: 50px; }
  .card--front .wordmark__main { font-size: 54px; }
  .card--front .wordmark__sub { font-size: 30px; }
  .card--back .wordmark { left: 196px; top: 180px; }
  .card--back .wordmark__main { font-size: 64px; }
  .card--back .wordmark__sub { font-size: 36px; }

  .person {
    position: absolute;
    right: 51px;
    top: 164px;
    text-align: right;
  }
  .person__name {
    color: var(--green);
    font-weight: 700;
    font-size: 23px;
    line-height: 28px;
    white-space: nowrap;
  }
  .person__role {
    margin-top: 2px;
    color: var(--ink);
    font-style: italic;
    font-size: 16px;
  }
  .person__rule {
    position: absolute;
    right: 51px;
    top: 256px;
    width: 38px;
    height: 3px;
    background: var(--green);
  }

  .contact-band {
    position: absolute;
    left: 0; right: 0; bottom: 0;
    height: 169px;
    background: var(--green);
    color: var(--white);
    font-size: 16.5px;
    line-height: 21px;
  }
  .contact {
    position: absolute;
    display: flex;
    align-items: center;
    gap: 10px;
    transform: translateY(-50%);
    white-space: nowrap;
  }
  .contact__icon { width: 23px; height: 23px; flex: none; }
  .divider {
    position: absolute;
    top: 45px;
    width: 1px;
    height: 55px;
    background: var(--divider);
  }
</style>
</head>
<body>

<section class="card card--front">
  <div class="wordmark">
    <span class="wordmark__main">Velorin</span>
    <span class="wordmark__sub">Adjusting</span>
  </div>

  <div class="person">
    <p class="person__name">Tariq S. AlHamdan (C.Eng., A.M.ASCE, MBA, FCCII)</p>
    <p class="person__name">Tariq S. AlHamdan (C.Eng., A.M.ASCE, MBA, FCCII)</p>
    <p class="person__role">Licensed Loss Adjuster &amp; Managing Partner</p>
  </div>
  <div class="person__rule"></div>

  <div class="contact-band">
    <div class="contact" style="left:53px; top:37px;">
      <svg class="contact__icon" viewBox="0 0 24 24"><circle cx="12" cy="12" r="12" fill="#fff"/><path d="M8.2 6.5l2 2.3-1.2 1.4c.8 1.8 2.1 3.1 3.9 3.9l1.4-1.2 2.3 2-1.3 2c-4.4-.4-8.6-4.6-9-9z" fill="#a9cb62"/></svg>
      <span>+(965) 22718450</span>
    </div>
    <div class="contact" style="left:53px; top:99px;">
      <svg class="contact__icon" viewBox="0 0 24 24"><circle cx="12" cy="12" r="12" fill="#fff"/><rect x="8.5" y="5.5" width="7" height="13" rx="1.2" fill="none" stroke="#a9cb62" stroke-width="1.6"/><circle cx="12" cy="16.2" r="0.9" fill="#a9cb62"/></svg>
      <span>+(965) 99127586<br>+(971) 552816304</span>
    </div>

    <div class="divider" style="left:227px;"></div>

    <div class="contact" style="left:263px; top:37px;">
      <svg class="contact__icon" viewBox="0 0 24 24"><circle cx="12" cy="12" r="12" fill="#fff"/><text x="12" y="16.5" text-anchor="middle" font-family="Carlito, sans-serif" font-size="14" fill="#a9cb62">@</text></svg>
      <span>tariq@velorin.com</span>
    </div>
    <div class="contact" style="left:263px; top:99px;">
      <svg class="contact__icon" viewBox="0 0 24 24"><circle cx="12" cy="12" r="12" fill="#fff"/><rect x="6" y="8" width="12" height="8.5" fill="none" stroke="#a9cb62" stroke-width="1.5"/><path d="M6 8l6 5 6-5M6 16.5l4.5-4M18 16.5l-4.5-4" fill="none" stroke="#a9cb62" stroke-width="1.3"/></svg>
      <span>P.O. Box 2518 Safat,<br>Kuwait 13026</span>
    </div>

    <div class="divider" style="left:456px;"></div>

    <div class="contact" style="left:489px; top:37px;">
      <svg class="contact__icon" viewBox="0 0 24 24"><circle cx="12" cy="12" r="12" fill="#fff"/><g fill="none" stroke="#a9cb62" stroke-width="1.3"><circle cx="12" cy="12" r="6.5"/><ellipse cx="12" cy="12" rx="2.8" ry="6.5"/><path d="M5.5 12h13M6.5 8.8h11M6.5 15.2h11"/></g></svg>
      <span>www.velorin.com</span>
    </div>
    <div class="contact" style="left:489px; top:99px;">
      <svg class="contact__icon" viewBox="0 0 24 24"><circle cx="12" cy="12" r="12" fill="#fff"/><rect x="8.5" y="5.5" width="7" height="4" fill="#a9cb62"/><rect x="6" y="10" width="12" height="5.5" rx="1" fill="#a9cb62"/><rect x="8.5" y="13.5" width="7" height="5" fill="#fff" stroke="#a9cb62" stroke-width="1.2"/></svg>
      <span>+(965) 25469031</span>
    </div>
  </div>
</section>

<section class="card card--back">
  <div class="wordmark">
    <span class="wordmark__main">Velorin</span>
    <span class="wordmark__sub">Adjusting</span>
  </div>
</section>

</body>
</html>
```